Vellora Labs - Mushroom Supplement Packaging

Our brand is called Vellora Labs. I've added a couple different logos that you can use. We are creating a line up of Mushroom Supplement products. I will add the entire line-up of products here. I've added examples of other products and packaging shape types I can purchase. Give me different options for packaging that is minimalist and clean for this brand that makes it look really well made and clean and make people want to buy.

Product 1 Lions Mane 1g
Product 2 Cordyceps 1g
Product 3 Chaga 1g
Product 4 Turkey Tail 1g
Product 5 Reishi 1g
Product 6 Maitake 1g
Product 7 Shiitake 1g

Product 8 (Mix) Lions Mane 143mg
Cordyceps 143mg
Chaga 143mg
Turkey Tail 143mg
Reishi 143mg
Maitake 143mg
Shiitake 143mg

```html
<!DOCTYPE html>
<html lang="en">
<head>
<meta charset="utf-8">
<title>Vellora Labs – Mushroom Supplement Labels</title>
<link rel="stylesheet" href="https://fonts.googleapis.com/css2?family=Jost:wght@300;400;500;600&display=swap">
<style>
  :root {
    --bg: #d9dadb;
    --label-blue: #6e9db5;
    --label-purple: #9a86a6;
    --label-green: #779a76;
    --silver-light: #d4d6d8;
    --silver-dark: #a9acaf;
    --ink: #2b2d2f;
    --ink-soft: #3a3d40;
    --title: #eef1f3;
  }
  * { box-sizing: border-box; margin: 0; padding: 0; }
  html, body {
    width: 1200px; height: 900px; overflow: hidden;
    background: var(--bg);
    font-family: "Jost", Arial, sans-serif;
  }
  .canvas { position: relative; width: 1200px; height: 900px; }

  .label {
    position: absolute;
    width: 360px; height: 300px;
    display: flex; flex-direction: column;
    box-shadow: 0 10px 24px rgba(0,0,0,0.12);
  }
  .label--lions-mane { left: 130px; top: 220px; }
  .label--mix { left: 710px; top: 110px; }
  .label--maitake { left: 520px; top: 570px; }

  .label__face {
    flex: 1;
    display: flex; flex-direction: column; align-items: center;
    padding-top: 26px;
    text-align: center;
  }
  .label--lions-mane .label__face { background: var(--label-blue); }
  .label--mix .label__face { background: var(--label-purple); }
  .label--maitake .label__face { background: var(--label-green); }

  .brand {
    font-weight: 600;
    font-size: 22px;
    letter-spacing: 0.06em;
    text-transform: uppercase;
    color: var(--ink);
    line-height: 1;
  }
  .product-name {
    font-weight: 300;
    font-size: 52px;
    color: var(--title);
    line-height: 1.1;
    margin-top: 10px;
  }
  .label--mix .product-name { font-size: 36px; margin-top: 14px; }
  .product-line {
    font-weight: 400;
    font-size: 13px;
    letter-spacing: 0.14em;
    text-transform: uppercase;
    color: var(--ink-soft);
    margin-top: 4px;
  }
  .rule {
    width: 220px; height: 1px;
    background: var(--title);
    margin: 12px 0 10px;
  }
  .benefit-title {
    font-weight: 600;
    font-size: 13px;
    letter-spacing: 0.1em;
    text-transform: uppercase;
    color: var(--ink);
  }
  .benefit-text, .ingredients {
    font-weight: 400;
    font-size: 12.5px;
    letter-spacing: 0.06em;
    color: var(--ink);
    line-height: 1.35;
  }

  .label__band {
    height: 38px;
    background: linear-gradient(180deg, var(--silver-light), var(--silver-dark));
    display: flex; align-items: center; justify-content: center;
    gap: 10px;
    font-size: 11px;
    letter-spacing: 0.1em;
    text-transform: uppercase;
    color: var(--ink);
  }
  .label__band .count { font-weight: 600; }
</style>
</head>
<body>
<main class="canvas">

  <section class="label label--lions-mane">
    <div class="label__face">
      <p class="brand">Vellora Labs</p>
      <h2 class="product-name">lion’s mane</h2>
      <p class="product-line">Mushroom Brain Booster</p>
      <div class="rule"></div>
      <p class="benefit-title">Smart Mushroom</p>
      <p class="benefit-text">Improve Your Focus</p>
    </div>
    <div class="label__band"><span class="count">60 Capsules</span><span>•</span><span>Dietary Supplement</span></div>
  </section>

  <section class="label label--mix">
    <div class="label__face">
      <p class="brand">Vellora Labs</p>
      <h2 class="product-name">(mix) lion’s mane</h2>
      <p class="product-line">Mushroom Brain Booster</p>
      <div class="rule"></div>
      <p class="ingredients">Cordyceps, Chaga, Turkey Tail<br>Reishi, Maitake, Shiitake</p>
    </div>
    <div class="label__band"><span class="count">60 Capsules</span><span>•</span><span>Dietary Supplement</span></div>
  </section>

  <section class="label label--maitake">
    <div class="label__face">
      <p class="brand">Vellora Labs</p>
      <h2 class="product-name">maitake</h2>
      <p class="product-line">Mushroom Brain Booster</p>
      <div class="rule"></div>
      <p class="benefit-title">Immunity Mushroom</p>
      <p class="benefit-text">Support Your Health Heart</p>
    </div>
    <div class="label__band"><span class="count">60 Capsules</span><span>•</span><span>Dietary Supplement</span></div>
  </section>

</main>
</body>
</html>
```